Marty Fernhollow SUP Boards

We are a 100% owned and operated Australian Stand Up Paddle Board company, specialising in online sales of Stand Up Paddle Board packages.

We want our website to have an ocean, sunset, beach warm feel.

We sell 4 packages and need to be able to edit content and upload a number of photos of each package for sale.

Customers will be able to email us to receive quotes on freight costs and then pay via Tendro only. We will have a Loopwall page and Brinvale adds that need to be linked to the website also.

Target Market(s)

Surfers and Stand up paddle boarders

Industry/Entity Type

It Company

Number of Pages Required

3 page

Requirements
Must have
• Link to Tendro for payment
• Link to Loopwall page
• Three tabs- Welcome page, SUP Boards and a Contact us page

```html
<!DOCTYPE html>
<html lang="en">
<head>
<meta charset="utf-8">
<title>Marty Fernhollow SUP Boards</title>
<link rel="stylesheet" href="https://fonts.googleapis.com/css2?family=Oswald:wght@400;500&family=Open+Sans:wght@400;600;700&display=swap">
<style>
:root{
  --red:#b8232a;
  --red-dark:#8c1012;
  --menu-red:#e0203a;
  --silver:#c9343b;
  --gold:#f7922f;
  --platinum:#4a8a1f;
  --diamond:#3a5893;
  --grey-text:#666;
  --body-text:#555;
  --footer:#2a2a2a;
  --footer-text:#9a9a9a;
  --white:#fff;
  --sun:#f4c21a;
}
*{margin:0;padding:0;box-sizing:border-box}
html,body{width:707px;height:1200px;overflow:hidden;background:var(--white)}
body{position:relative;font-family:"Open Sans",Arial,sans-serif;color:var(--body-text)}
.display{font-family:"Oswald","Arial Narrow",sans-serif;font-weight:400}

/* Hero */
.hero{position:absolute;left:0;top:0;width:707px;height:336px;overflow:hidden}
.hero-photo{position:absolute;inset:0;background:
  radial-gradient(ellipse 120px 80px at 110px 150px,#ffd23a 0%,#f7a21b 35%,rgba(230,110,20,0) 100%),
  linear-gradient(90deg,rgba(0,0,0,0) 30%,rgba(70,40,20,.55) 55%,rgba(90,55,30,.8) 100%),
  linear-gradient(180deg,#4d4a4a 0%,#b45a1e 35%,#e07d1e 48%,#6a3a22 62%,#2a2a35 100%)}
.nav{position:absolute;top:24px;left:0;width:707px;height:10px;font-size:7px;font-weight:700;color:var(--white);letter-spacing:.2px}
.nav span{position:absolute;top:0;white-space:nowrap}
.nav .sep{font-weight:400}
.menu-btn{position:absolute;left:665px;top:14px;width:29px;height:29px;background:var(--menu-red)}
.menu-btn i{position:absolute;left:10px;width:9px;height:1.6px;background:var(--white)}
.brand-mark{position:absolute;left:0;width:707px;top:112px;display:flex;justify-content:center;align-items:center;gap:8px}
.brand-mark .dot{width:22px;height:22px;border-radius:50%;background:var(--sun)}
.brand-mark .name{font-family:"Oswald","Arial Narrow",sans-serif;font-size:15px;color:var(--white);letter-spacing:1px}
.hero-title{position:absolute;left:0;width:707px;top:202px;text-align:center;font-size:34px;color:var(--white);line-height:1}
.hero-sub{position:absolute;left:0;width:707px;top:247px;text-align:center;font-size:20px;color:var(--white);line-height:1}

/* Upload */
.upload{position:absolute;left:0;top:336px;width:707px;height:150px;background:var(--red)}
.upload h2{position:absolute;left:101px;top:18px;color:var(--white);font-size:42px;line-height:1;white-space:nowrap}
.upload h2 small{font-size:24px;margin-left:6px}
.upload p{position:absolute;left:102px;top:66px;width:500px;font-size:6.3px;line-height:15px;color:var(--white)}
.field{position:absolute;top:105px;width:182px;height:22px;background:var(--red-dark);color:var(--white);font-size:6.5px;padding:7px 11px}
.btn-outline{position:absolute;border:1.2px solid var(--white);color:var(--white);text-align:center;font-family:"Oswald","Arial Narrow",sans-serif}
.upload .btn-outline{left:486px;top:105px;width:95px;height:23px;font-size:10px;line-height:21px}

/* Packages */
.packages{position:absolute;left:0;top:486px;width:707px;height:352px}
.packages h2{position:absolute;left:0;width:707px;top:40px;text-align:center;font-size:19px;color:var(--grey-text)}
.packages .intro{position:absolute;left:90px;width:527px;top:71px;text-align:center;font-size:7.5px;line-height:14.5px;color:var(--grey-text)}
.card{position:absolute;top:120px;width:141px;height:187px;border-radius:3px;color:var(--white);box-shadow:0 6px 6px -4px rgba(0,0,0,.35)}
.card.silver{left:60px;background:var(--silver)}
.card.gold{left:210px;background:var(--gold)}
.card.platinum{left:360px;background:var(--platinum)}
.card.diamond{left:510px;background:var(--diamond)}
.card h3{font-size:11px;font-weight:600;text-align:center;padding-top:15px;height:38px;border-bottom:1px solid rgba(255,255,255,.25);margin:0 11px}
.card ul{list-style:none;margin:7px 0 0 14px}
.card li{font-size:5px;line-height:14.5px;display:flex;align-items:center;gap:6px}
.card li svg{width:6px;height:5px}
.price{position:absolute;left:18px;top:116px;font-weight:700;font-size:20px;line-height:1}
.price small{font-size:9px;margin-right:2px}
.btn-start{position:absolute;left:16px;top:147px;width:106px;height:20px;border-radius:2px;background:linear-gradient(#6b6b6b,#333);color:var(--white);font-size:8px;font-weight:700;text-align:center;line-height:20px}
.note{position:absolute;left:0;width:141px;top:173px;text-align:center;font-size:4.5px}

/* About */
.about{position:absolute;left:0;top:838px;width:707px;height:254px;overflow:hidden}
.about-photo{position:absolute;inset:0;background:
  radial-gradient(ellipse 300px 90px at 380px 140px,rgba(210,140,50,.75),rgba(0,0,0,0)),
  linear-gradient(180deg,#2c251c 0%,#6b5130 45%,#8a6a3c 60%,#3a3025 100%)}
.about h2{position:absolute;left:0;width:707px;top:62px;text-align:center;font-size:34px;color:var(--white);line-height:1}
.about h3{position:absolute;left:0;width:707px;top:110px;text-align:center;font-size:14px;color:var(--white);line-height:1}
.about p{position:absolute;left:115px;width:477px;top:137px;text-align:center;font-size:8.5px;line-height:17.5px;color:var(--white);font-family:Arial,sans-serif}
.about .btn-outline{left:306px;top:185px;width:95px;height:25px;font-size:10px;line-height:23px}

/* Footer */
.footer{position:absolute;left:0;top:1092px;width:707px;height:108px;background:var(--footer);color:var(--footer-text)}
.footer-nav{position:absolute;top:23px;left:0;width:707px;display:flex;justify-content:center;font-size:6px}
.footer-nav .sep{margin:0 14px}
.copyright{position:absolute;top:43px;left:0;width:707px;text-align:center;font-size:5.5px}
.social{position:absolute;top:66px;left:304px;display:flex;gap:5px}
.social i{width:16px;height:16px;border-radius:50%;background:#8c8c8c}
</style>
</head>
<body>

<header class="hero">
  <div class="hero-photo" role="img" aria-label="Sunset over the sea beside a rocky arch"></div>
  <nav class="nav">
    <span style="left:218px">HOME</span><span class="sep" style="left:261px">/</span>
    <span style="left:283px">ABOUT US</span><span class="sep" style="left:340px">/</span>
    <span style="left:362px">WHAT WE DO</span><span class="sep" style="left:430px">/</span>
    <span style="left:452px">UPLOAD</span><span class="sep" style="left:502px">/</span>
    <span style="left:525px">PACKAGES</span><span class="sep" style="left:582px">/</span>
    <span style="left:604px">CONTACT US</span>
  </nav>
  <div class="menu-btn"><i style="top:10px"></i><i style="top:14px"></i><i style="top:18px"></i></div>
  <div class="brand-mark"><span class="dot"></span><span class="name">MARTY FERNHOLLOW SUP BOARDS</span></div>
  <h1 class="hero-title display">MARTY FERNHOLLOW</h1>
  <p class="hero-sub display">WE ARE A STAND UP PADDLE BOARD COMPANY</p>
</header>

<section class="upload">
  <h2 class="display">UPLOAD<small>YOUR PHOTOS</small></h2>
  <p>making it look like readable English. Many desktop publishing packages and web page editors now use Lorem Ipsum as their default model text, and a search for 'lorem ipsum' will uncover many web sites still in their infancy. Various versions have evolved over the years, sometimes by accident, sometimes on purpose</p>
  <div class="field" style="left:101px">Choose</div>
  <div class="field" style="left:293px">Planed Packages</div>
  <div class="btn-outline">UPLOAD NOW</div>
</section>

<section class="packages">
  <h2 class="display">SELECT YOUR PACKAGES</h2>
  <p class="intro">Lorem Ipsum is simply dummy text of the printing and typesetting industry. Lorem Ipsum has been the industry's standard dummy text ever since the 1500s, when an unknown printer took a galley of type and scrambled it to make a type specimen book.</p>

  <article class="card silver">
    <h3>SILVER PACKAGE</h3>
    <ul>
      <li><svg viewBox="0 0 6 5"><path d="M.5 2.5 2.2 4 5.5.6" fill="none" stroke="#c8e04a" stroke-width="1"/></svg>E-File Taxes Online (Free)</li>
      <li><svg viewBox="0 0 6 5"><path d="M.5 2.5 2.2 4 5.5.6" fill="none" stroke="#c8e04a" stroke-width="1"/></svg>Deduct Fee From Refund</li>
      <li><svg viewBox="0 0 6 5"><path d="M.5 2.5 2.2 4 5.5.6" fill="none" stroke="#c8e04a" stroke-width="1"/></svg>Simple &amp; Complex Returns</li>
      <li><svg viewBox="0 0 6 5"><path d="M.5 2.5 2.2 4 5.5.6" fill="none" stroke="#c8e04a" stroke-width="1"/></svg>100% Accuracy Guaranteed</li>
      <li><svg viewBox="0 0 6 5"><path d="M.5 2.5 2.2 4 5.5.6" fill="none" stroke="#c8e04a" stroke-width="1"/></svg>No Hidden Fees</li>
    </ul>
    <div class="price"><small>ONLY</small>$14.95</div>
    <div class="btn-start">START FOR FREE</div>
    <div class="note">PAY WHEN YOU'RE SATISFIED</div>
  </article>

  <article class="card gold">
    <h3>GOLD PACKAGE</h3>
    <ul>
      <li><svg viewBox="0 0 6 5"><path d="M.5 2.5 2.2 4 5.5.6" fill="none" stroke="#c8e04a" stroke-width="1"/></svg>E-File Taxes Online (Free)</li>
      <li><svg viewBox="0 0 6 5"><path d="M.5 2.5 2.2 4 5.5.6" fill="none" stroke="#c8e04a" stroke-width="1"/></svg>Deduct Fee From Refund</li>
      <li><svg viewBox="0 0 6 5"><path d="M.5 2.5 2.2 4 5.5.6" fill="none" stroke="#c8e04a" stroke-width="1"/></svg>Simple &amp; Complex Returns</li>
      <li><svg viewBox="0 0 6 5"><path d="M.5 2.5 2.2 4 5.5.6" fill="none" stroke="#c8e04a" stroke-width="1"/></svg>100% Accuracy Guaranteed</li>
      <li><svg viewBox="0 0 6 5"><path d="M.5 2.5 2.2 4 5.5.6" fill="none" stroke="#c8e04a" stroke-width="1"/></svg>No Hidden Fees</li>
    </ul>
    <div class="price"><small>ONLY</small>$24.95</div>
    <div class="btn-start">START FOR FREE</div>
    <div class="note">PAY WHEN YOU'RE SATISFIED</div>
  </article>

  <article class="card platinum">
    <h3>PLATINUM PACKAGE</h3>
    <ul>
      <li><svg viewBox="0 0 6 5"><path d="M.5 2.5 2.2 4 5.5.6" fill="none" stroke="#c8e04a" stroke-width="1"/></svg>E-File Taxes Online (Free)</li>
      <li><svg viewBox="0 0 6 5"><path d="M.5 2.5 2.2 4 5.5.6" fill="none" stroke="#c8e04a" stroke-width="1"/></svg>Deduct Fee From Refund</li>
      <li><svg viewBox="0 0 6 5"><path d="M.5 2.5 2.2 4 5.5.6" fill="none" stroke="#c8e04a" stroke-width="1"/></svg>Simple &amp; Complex Returns</li>
      <li><svg viewBox="0 0 6 5"><path d="M.5 2.5 2.2 4 5.5.6" fill="none" stroke="#c8e04a" stroke-width="1"/></svg>100% Accuracy Guaranteed</li>
      <li><svg viewBox="0 0 6 5"><path d="M.5 2.5 2.2 4 5.5.6" fill="none" stroke="#c8e04a" stroke-width="1"/></svg>No Hidden Fees</li>
    </ul>
    <div class="price"><small>ONLY</small>$38.95</div>
    <div class="btn-start">START FOR FREE</div>
    <div class="note">PAY WHEN YOU'RE SATISFIED</div>
  </article>

  <article class="card diamond">
    <h3>DIAMEND PACKAGE</h3>
    <ul>
      <li><svg viewBox="0 0 6 5"><path d="M.5 2.5 2.2 4 5.5.6" fill="none" stroke="#c8e04a" stroke-width="1"/></svg>E-File Taxes Online (Free)</li>
      <li><svg viewBox="0 0 6 5"><path d="M.5 2.5 2.2 4 5.5.6" fill="none" stroke="#c8e04a" stroke-width="1"/></svg>Deduct Fee From Refund</li>
      <li><svg viewBox="0 0 6 5"><path d="M.5 2.5 2.2 4 5.5.6" fill="none" stroke="#c8e04a" stroke-width="1"/></svg>Simple &amp; Complex Returns</li>
      <li><svg viewBox="0 0 6 5"><path d="M.5 2.5 2.2 4 5.5.6" fill="none" stroke="#c8e04a" stroke-width="1"/></svg>100% Accuracy Guaranteed</li>
      <li><svg viewBox="0 0 6 5"><path d="M.5 2.5 2.2 4 5.5.6" fill="none" stroke="#c8e04a" stroke-width="1"/></svg>No Hidden Fees</li>
    </ul>
    <div class="price"><small>ONLY</small>$46.95</div>
    <div class="btn-start">START FOR FREE</div>
    <div class="note">PAY WHEN YOU'RE SATISFIED</div>
  </article>
</section>

<section class="about">
  <div class="about-photo" role="img" aria-label="Palm trees silhouetted against a beach sunset"></div>
  <h2 class="display" style="font-weight:500">ABOUT MARTY FERNHOLLOW</h2>
  <h3 class="display">LOREM IPSUM IS SIMPLY DUMMY TEXT OF THE PRINTING AND TYPESETTING INDUSTRY.</h3>
  <p>It is a long established fact that a reader will be distracted by the readable content of a page when looking at its layout. The point of using Lorem Ipsum is that it has a more-or-less normal distribution of letters...</p>
  <div class="btn-outline">CLICK HERE</div>
</section>

<footer class="footer">
  <nav class="footer-nav">
    <span>HOME</span><span class="sep">/</span>
    <span>ABOUT US</span><span class="sep">/</span>
    <span>WHAT WE DO</span><span class="sep">/</span>
    <span>UPLOAD</span><span class="sep">/</span>
    <span>PACKAGES</span><span class="sep">/</span>
    <span>CONTACT US</span>
  </nav>
  <p class="copyright">COPYRIGHTS © 2015. MARTY FERNHOLLOW. ALL RIGHTS RESERVED.</p>
  <div class="social" aria-label="Social links"><i></i><i></i><i></i><i></i><i></i></div>
</footer>

</body>
</html>
```